Law Firm Logo and Stationary

I need a logo for my law firm.  The logo should only contain the firm name "Halvey & Halvey, P.C." but we are open to slight additions like underlining or a box.  We are looking for a modern style but not edgy because our target market is businesses and corporations.

I would like a logo that invokes the traditional values of a law firm (trust, integrity, knowledge) but I want an updated look.

To be clear, the logo should only contain the firm name, I am just looking for a font treatment.

The logo color is up to you.  The only initial opinion I have is that bright colors may not fit with the professional look of a law firm. 

I also want to incorporate the new logo into letterhead and business card designs.  The letterhead should include all of the information that is in my current letterhead, which is attached.  The letterhead should be black or grey on white.  The colored logo will go on the website and promotional materials.

For the business card, I would like to have the logo on the top left, the employee name (Colin T. Halvey) on the middle left and the firm information (address, tel, fax, website, email) on right side.  I am open to suggestions if you have better ideas.
Updates

Here are some comments on the initial 8 designs:

a) I am just interested in a font treatment of our firm name, "Halvey & Halvey, P.C."  I do not want any graphics like a gavel or shield. 

b) The full name of the firm must be in the logo.  So I cannot use designs that only have "H & H"

c) EXAMPLES: Here are two websites with examples of law firm logos that just have the firm name.  These are just samples to give you a general idea of what I am looking for.  Check out:  www.qz-legal.example and www.marrowfieldtate.example 

In short, I am looking for a simple, clean design that will look modern enough for our website but is also conservative enough to be on letterhead that gets sent to judges and other lawyers.

Also, the sample letterhead is now loaded in the brief so you can see the information I need included in the new letterhead.

Thanks.

Target Market(s)

businesses and corporations.

Industry/Entity Type

Law Firm

Logo Text

Halvey & Halvey, P.C.

Requirements
Must have
• Firm name, "Halvey & Halvey, P.C."

```html
<!DOCTYPE html>
<html lang="en">
<head>
<meta charset="utf-8">
<title>Halvey &amp; Halvey PC — Identity and Stationery</title>
<link rel="stylesheet" href="https://fonts.googleapis.com/css2?family=Oswald:wght@300;400&display=swap">
<style>
  :root {
    --ink: #463d36;
    --gold: #a8956f;
    --paper: #ffffff;
    --card-text: #f4f1ec;
  }
  * { margin: 0; padding: 0; box-sizing: border-box; }
  html, body { width: 848px; height: 1200px; overflow: hidden; background: var(--paper); }
  body { position: relative; font-family: "Oswald", sans-serif; font-weight: 300; color: var(--ink); }

  .wordmark { position: absolute; display: block; overflow: visible; }
  .wordmark text { font-family: "Oswald", sans-serif; font-weight: 300; }
  .wordmark--hero { left: 70px; top: 120px; }
  .wordmark--letterhead { left: 152px; top: 276px; }
  .wordmark--card { left: 496px; top: 497px; }

  .letterhead {
    position: absolute; left: 123px; top: 213px;
    width: 638px; height: 903px;
    border: 1px solid var(--ink);
  }
  .letterhead__rule {
    position: absolute; left: 238px; top: 30px;
    width: 1px; height: 91px; background: var(--gold);
  }
  .letterhead__masthead { position: absolute; left: 246px; top: 46px; line-height: 1; }
  .letterhead__title { font-size: 15px; letter-spacing: 0.5px; margin-bottom: 4px; }
  .letterhead__line { font-size: 7.2px; letter-spacing: 0.3px; line-height: 9.2px; }
  .letterhead__line--admit { font-size: 8px; }
  .letterhead__footer {
    position: absolute; left: 21px; top: 786px;
    font-size: 13px; line-height: 15.5px; letter-spacing: 0.4px;
  }

  .card { position: absolute; left: 465px; width: 320px; height: 156px; background: var(--ink); }
  .card--front { top: 433px; }
  .card--back { top: 598px; }
  .card__divider { position: absolute; left: 158px; top: 0; width: 1px; height: 100%; background: var(--card-text); }
  .card__name {
    position: absolute; left: 20px; top: 74px;
    font-size: 14px; letter-spacing: 0.6px; color: var(--card-text); line-height: 1;
  }
  .card__contact {
    position: absolute; left: 175px; top: 48px;
    font-size: 8.8px; line-height: 11.3px; letter-spacing: 0.3px; color: var(--gold);
  }
</style>
</head>
<body>

  <svg class="wordmark wordmark--hero" width="450" height="60" aria-label="Halvey &amp; Halvey PC">
    <text x="0" y="51" font-size="60" fill="var(--ink)" textLength="444" lengthAdjust="spacing">HALVEY &amp; HALVEY PC</text>
  </svg>

  <section class="letterhead">
    <div class="letterhead__rule"></div>
    <div class="letterhead__masthead">
      <p class="letterhead__title">LAW OFFICES</p>
      <p class="letterhead__line">WARREN E. HALVEY</p>
      <p class="letterhead__line">COLIN T. HALVEY</p>
      <p class="letterhead__line">SAMUEL HALVEY (1916-1994)</p>
      <p class="letterhead__line letterhead__line--admit">Admitted to practice District of Columbia . Maryland . New York</p>
    </div>
    <address class="letterhead__footer" style="font-style:normal">
      2750 Alder Avenue<br>
      Brookfield, MD 20915<br>
      T: 301.555.0142<br>
      F: 301.555.0187<br>
      E: warren.halvey@halveypc.example<br>
      www.halveypc.example
    </address>
  </section>

  <svg class="wordmark wordmark--letterhead" width="200" height="30" aria-label="Halvey &amp; Halvey PC">
    <text x="0" y="25" font-size="27" fill="var(--ink)" textLength="197" lengthAdjust="spacing">HALVEY &amp; HALVEY PC</text>
  </svg>

  <div class="card card--front"></div>
  <svg class="wordmark wordmark--card" width="260" height="36" aria-label="Halvey &amp; Halvey PC">
    <text x="0" y="31" font-size="34" fill="var(--card-text)" textLength="255" lengthAdjust="spacing">HALVEY &amp; HALVEY PC</text>
  </svg>

  <div class="card card--back">
    <div class="card__divider"></div>
    <p class="card__name">WARREN E. HALVEY</p>
    <address class="card__contact" style="font-style:normal">
      2750 Alder Avenue<br>
      Brookfield, MD 20915<br>
      T: 301.555.0142<br>
      F: 301.555.0187<br>
      E: warren.halvey@halveypc.example<br>
      www.halveypc.example
    </address>
  </div>

</body>
</html>
```